Zielgruppe
Wir sind ein Vertriebsunternehmen, mit dem Ziel die klassische Finanz und den Kryptosektor zu verbinden. Unsere Zielgruppe sind Menschen zwischn 25 - 45 Jahre.
Aufgabenstellung
Wir sind ein Vertriebsunternehmen, mit dem Ziel die klassische Finanz und den Kryptosektor zu verbinden. Unsere Zielgruppe sind Menschen zwischn 25 - 45 Jahre. Wir sind die Communty und Vertrieb der ersten rechtkonformen STO - Plattform ( Plattform für Wertpapiere im Kryptosektor)
Diese Projekt ist Teil eines Paketes, wir bitten nur Designer mit zu machen die alle benötigten Unterlagen designen können.
Online-Marketing Material
2 Vorlagen Social Media - (Einladung/Event, Sprüche/Information)
Banner
Präsentationsvorlagen - min unterschiedliche 8 Vorlagenseiten /Layouts.
Landingpage Layout f. Funnelsite für Webinaranmeldung mit Platz für Formular
Newsletter Layoutvorlage
Vorlage Infografik
Broschüre / E - Book Designe
Es werden nur Vorlagen benötigt mit 'LoremSum Texten' und Musterbildern. Wir möchten von allen Vorlagen die Originaldatei, uns stehen folgende Grafikprogramme zur Verfügung:
Adobe Photoshop
Adobe Illustrator
Canva
Unsere Akt. Designe (Designe Alt) gefällt uns von der Idee, dennoch wünschen wir es uns moderner und edler mit ein wenig 'spaceig'. - Eben die Vereinigung von Kryptowelt und klassischer Finanz.
Schriftart: Poppins
Farben lt. Logo

```html
<!DOCTYPE html>
<html lang="de">
<head>
<meta charset="utf-8">
<title>Team-Profile – Silber Kranich Investments</title>
<link href="https://fonts.googleapis.com/css2?family=Poppins:wght@400;500;600;700&display=swap" rel="stylesheet">
<style>
:root{
  --canvas-bg:#ffffff;
  --sidebar-bg:#dcdfe9;
  --sidebar-edge:#f4f5fa;
  --header-bg:#d6d9e4;
  --brand-blue:#1f4fa8;
  --band-blue:#2563c9;
  --ink:#2a2d36;
  --muted:#5a5e69;
  --rule-dark:#2d3440;
  --rule-mid:#7d8592;
  --rule-light:#c3c9d3;
}
*{box-sizing:border-box;margin:0;padding:0}
html,body{width:1200px;height:3142px;overflow:hidden;background:var(--canvas-bg);font-family:"Poppins",sans-serif;color:var(--ink)}
.profile{position:absolute;left:109px;width:982px;height:1390px;background:linear-gradient(180deg,#e3e5ef 0%,#eceef4 100%);overflow:hidden}
.profile--first{top:104px}
.profile--second{top:1594px}
.brand-band{position:absolute;left:0;right:0;top:1203px;height:96px;background:linear-gradient(90deg,var(--band-blue),#3a78dc 50%,var(--band-blue))}
.sidebar{position:absolute;left:26px;top:26px;width:334px;height:1335px;background:var(--sidebar-bg);border:5px solid var(--sidebar-edge);border-radius:18px;box-shadow:0 6px 18px rgba(40,50,80,.12);padding:0 24px}
.portrait{display:block;margin:62px auto 0;width:208px;height:196px}
.role{text-align:center;font-size:18.5px;line-height:30px;margin:14px auto 0;max-width:230px}
.role strong{display:block;font-weight:600;letter-spacing:.2px;white-space:nowrap;margin:0 -30px}
.role .spaced{letter-spacing:5px}
.side-title{font-size:29px;font-weight:600;margin-top:72px;line-height:40px}
.profile--second .side-title.first{margin-top:40px}
.side-text{font-size:19.6px;line-height:34.8px;margin-top:6px}
.side-title + .side-list{margin-top:10px}
.side-list{font-size:19.6px;line-height:34.8px;list-style:none}
.sidebar .side-title.projects{margin-top:60px}
.header-panel{position:absolute;left:360px;top:53px;width:597px;height:190px;background:var(--header-bg);border-radius:0 6px 6px 0;padding:32px 0 0 26px}
.name{font-size:34px;font-weight:600;line-height:31px;color:var(--brand-blue);letter-spacing:.5px}
.rules{display:flex;gap:6px;margin-top:8px}
.rules span{height:6px;border-radius:3px}
.rules span:nth-child(1){width:80px;background:var(--rule-dark)}
.rules span:nth-child(2){width:46px;background:var(--rule-mid)}
.rules span:nth-child(3){width:16px;background:var(--rule-light)}
.tagline{font-size:27px;margin-top:8px}
.main{position:absolute;left:394px;top:275px;width:570px}
.section-head{display:flex;align-items:center;gap:14px;height:92px}
.section-head svg{width:86px;height:92px;flex:none}
.section-head h2{font-size:30px;font-weight:600}
.about{font-size:20.3px;line-height:34.8px;margin-top:24px}
.career{margin-top:32px}
.career .section-head{margin-bottom:14px}
.entry{margin-bottom:8px}
.entry .date{font-size:20px;line-height:28px}
.entry .degree{font-size:19.8px;line-height:24px;padding-left:38px}
.entry .school{font-size:17.5px;line-height:21px;padding-left:38px;color:var(--muted)}
.contact{margin-top:58px}
.contact ul{list-style:none;margin-top:16px}
.contact li{display:flex;align-items:center;gap:14px;font-size:20px;line-height:35px}
.contact li svg{width:22px;height:22px;flex:none}
.footer-card{position:absolute;left:386px;top:1190px;width:571px;height:122px;background:#f4f5fa;border-radius:18px;box-shadow:0 4px 14px rgba(30,60,120,.18);text-align:center;padding-top:20px}
.footer-brand{display:flex;align-items:center;justify-content:center;gap:12px}
.footer-brand .dot{width:30px;height:30px;border-radius:50%;background:var(--brand-blue)}
.footer-brand span{font-size:27px;font-weight:600;color:var(--ink)}
.footer-claim{font-size:15px;color:var(--muted);margin-top:0}
.footer-copy{font-size:16px;color:var(--brand-blue);margin-top:4px}
</style>
</head>
<body>

<svg width="0" height="0" style="position:absolute">
  <defs>
    <linearGradient id="badge-fill" x1="0" y1="0" x2="0" y2="1">
      <stop offset="0" stop-color="#7fa3e6"/>
      <stop offset="1" stop-color="#3f6fcb"/>
    </linearGradient>
    <symbol id="badge" viewBox="0 0 86 92">
      <path d="M43 3 Q47 3 51 5 L77 20 Q83 24 83 31 L83 61 Q83 68 77 72 L51 87 Q43 91 35 87 L9 72 Q3 68 3 61 L3 31 Q3 24 9 20 L35 5 Q39 3 43 3Z" fill="url(#badge-fill)"/>
    </symbol>
  </defs>
</svg>

<!-- Profil 1 -->
<article class="profile profile--first">
  <div class="brand-band"></div>
  <aside class="sidebar">
    <svg class="portrait" viewBox="0 0 208 196" role="img" aria-label="Porträtfoto des Gründers vor grünem Hintergrund">
      <defs><linearGradient id="photo-a" x1="0" y1="0" x2="0" y2="1"><stop offset="0" stop-color="#4d6b35"/><stop offset=".6" stop-color="#7a6a5a"/><stop offset="1" stop-color="#3d6aa8"/></linearGradient></defs>
      <path d="M104 2 L204 48 L204 148 L104 194 L4 148 L4 48Z" fill="url(#photo-a)"/>
    </svg>
    <p class="role"><strong class="spaced">CEO</strong><strong>SILBERKRANICH INVEST</strong>Unsere Mission ist die Verbindung der klassischen Finanz und der Krypto Welt</p>
    <h3 class="side-title">Zuständigkeit</h3>
    <p class="side-text">Lorem ipsum dolor sitamet consetetur sadipscing elitr diam nonumy eirmod tem invidunt ut labore et dolori magna aliquyam erat, sed diam voluptua. At vero eos accusam et justo duo estil et ea rebum. Stet clita kas gubergren, no sea takimat sanctus est Lorem ipsum il sit amet.</p>
    <h3 class="side-title projects">aktuelle Projekte</h3>
    <ul class="side-list"><li>Silber Kranich Investment</li><li>Wegnotiz.at - der Blog für alle die aktiv Wachsen wollen.</li><li>Lichtwandelfotografie</li></ul>
  </aside>
  <header class="header-panel">
    <h1 class="name">TOBIAS<br>WENDLER</h1>
    <div class="rules"><span></span><span></span><span></span></div>
    <p class="tagline">Gründer - Silber Kranich Investment</p>
  </header>
  <div class="main">
    <section>
      <div class="section-head"><svg viewBox="0 0 86 92"><use href="#badge"/><circle cx="43" cy="36" r="11" fill="#dfe8fb"/><path d="M24 66 Q24 50 43 50 Q62 50 62 66Z" fill="#dfe8fb"/></svg><h2>Über Mich</h2></div>
      <p class="about">Lorem ipsum dolor sit amet, consetetur sadipscing elitr, sed diam nonumy eirmod tempor invidunt ut labore et dolore magna aliquyam erat, sed diam voluptua. At vero eos et accusam et justo duo dolores et ea rebum. Stet clita kasd gubergren, no sea takimata sanctus est Lorem ipsum dolor sit amet.</p>
    </section>
    <section class="career">
      <div class="section-head"><svg viewBox="0 0 86 92"><use href="#badge"/><rect x="22" y="34" width="42" height="30" rx="4" fill="#dfe8fb"/><rect x="35" y="27" width="16" height="8" rx="2" fill="none" stroke="#dfe8fb" stroke-width="3"/><rect x="22" y="46" width="42" height="3" fill="#6b90d8"/></svg><h2>Berufserfahrung</h2></div>
      <div class="entry"><p class="date">10 / 2015 – 06 / 2018</p><p class="degree">Master of Arts in Marketing</p><p class="school">Universität zu Jede Stadt</p></div>
      <div class="entry"><p class="date">10 / 2012 – 06 / 2015</p><p class="degree">Bachelor of Arts in Marketing</p><p class="school">Universität zu Jede Stadt</p></div>
    </section>
    <section class="contact">
      <div class="section-head"><svg viewBox="0 0 86 92"><use href="#badge"/><path d="M20 44 L32 34 L44 40 L54 34 L66 44 L52 60 Q48 64 44 60 L30 54Z" fill="#dfe8fb"/></svg><h2>Kontakt</h2></div>
      <ul>
        <li><svg viewBox="0 0 24 24"><path d="M6 2 L10 2 L11 7 L8 9 Q10 14 15 16 L17 13 L22 14 L22 18 Q22 22 18 22 Q3 20 2 6 Q2 2 6 2Z" fill="#2a2d36"/></svg>(01) 0123 456 789</li>
        <li><svg viewBox="0 0 24 24"><circle cx="12" cy="12" r="9" fill="none" stroke="#2a2d36" stroke-width="2.6"/><circle cx="12" cy="12" r="3.5" fill="none" stroke="#2a2d36" stroke-width="2.6"/></svg>lorem@silberkranich.investments</li>
        <li><svg viewBox="0 0 24 24"><rect x="2" y="2" width="20" height="20" rx="2" fill="#2a2d36"/></svg>@MusterProfil</li>
      </ul>
    </section>
  </div>
  <footer class="footer-card">
    <div class="footer-brand"><i class="dot"></i><span>Silber Kranich Investments</span></div>
    <p class="footer-claim">Ihr Partner für digitale Werte</p>
    <p class="footer-copy">© 2023 Silber Kranich Investments. Alle Rechte vorbehalten</p>
  </footer>
</article>

<!-- Profil 2 -->
<article class="profile profile--second">
  <div class="brand-band"></div>
  <aside class="sidebar">
    <svg class="portrait" viewBox="0 0 208 196" role="img" aria-label="Schwarzweiß-Porträtfoto der Leiterin Operations">
      <defs><linearGradient id="photo-b" x1="0" y1="0" x2="0" y2="1"><stop offset="0" stop-color="#3a3a3a"/><stop offset=".5" stop-color="#9a9a9a"/><stop offset="1" stop-color="#1c1c1c"/></linearGradient></defs>
      <path d="M104 2 L204 48 L204 148 L104 194 L4 148 L4 48Z" fill="url(#photo-b)"/>
    </svg>
    <p class="role"><strong>HEAD OF OPERATIONS</strong><strong>TEAMMANAGEMENT</strong><strong>SILBERKRANICH INVEST</strong>Unsere Mission ist die Verbindung der klassischen Finanz und der Krypto Welt</p>
    <h3 class="side-title first">Zuständigkeit</h3>
    <p class="side-text">Lorem ipsum dolor sitamet consetetur sadipscing elitr diam nonumy eirmod tem invidunt ut labore et dolori magna aliquyam erat, sed diam voluptua. At vero eos accusam et justo duo estil et ea rebum. Stet clita kas gubergren, no sea takimat sanctus est Lorem ipsum il sit amet.</p>
    <h3 class="side-title projects">aktuelle Projekte</h3>
    <ul class="side-list"><li>Silber Kranich Investment</li><li>Wegnotiz.at - der Blog für alle die aktiv Wachsen wollen.</li><li>Lichtwandelfotografie</li></ul>
  </aside>
  <header class="header-panel">
    <h1 class="name">MIRIAM<br>KESSLER</h1>
    <div class="rules"><span></span><span></span><span></span></div>
    <p class="tagline">Gründer - Silber Kranich Investment</p>
  </header>
  <div class="main">
    <section>
      <div class="section-head"><svg viewBox="0 0 86 92"><use href="#badge"/><circle cx="43" cy="36" r="11" fill="#dfe8fb"/><path d="M24 66 Q24 50 43 50 Q62 50 62 66Z" fill="#dfe8fb"/></svg><h2>Über Mich</h2></div>
      <p class="about">Lorem ipsum dolor sit amet, consetetur sadipscing elitr, sed diam nonumy eirmod tempor invidunt ut labore et dolore magna aliquyam erat, sed diam voluptua. At vero eos et accusam et justo duo dolores et ea rebum. Stet clita kasd gubergren, no sea takimata sanctus est Lorem ipsum dolor sit amet.</p>
    </section>
    <section class="career">
      <div class="section-head"><svg viewBox="0 0 86 92"><use href="#badge"/><rect x="22" y="34" width="42" height="30" rx="4" fill="#dfe8fb"/><rect x="35" y="27" width="16" height="8" rx="2" fill="none" stroke="#dfe8fb" stroke-width="3"/><rect x="22" y="46" width="42" height="3" fill="#6b90d8"/></svg><h2>Berufserfahrung</h2></div>
      <div class="entry"><p class="date">10 / 2015 – 06 / 2018</p><p class="degree">Master of Arts in Marketing</p><p class="school">Universität zu Jede Stadt</p></div>
      <div class="entry"><p class="date">10 / 2012 – 06 / 2015</p><p class="degree">Bachelor of Arts in Marketing</p><p class="school">Universität zu Jede Stadt</p></div>
    </section>
    <section class="contact">
      <div class="section-head"><svg viewBox="0 0 86 92"><use href="#badge"/><path d="M20 44 L32 34 L44 40 L54 34 L66 44 L52 60 Q48 64 44 60 L30 54Z" fill="#dfe8fb"/></svg><h2>Kontakt</h2></div>
      <ul>
        <li><svg viewBox="0 0 24 24"><path d="M6 2 L10 2 L11 7 L8 9 Q10 14 15 16 L17 13 L22 14 L22 18 Q22 22 18 22 Q3 20 2 6 Q2 2 6 2Z" fill="#2a2d36"/></svg>(01) 0123 456 789</li>
        <li><svg viewBox="0 0 24 24"><circle cx="12" cy="12" r="9" fill="none" stroke="#2a2d36" stroke-width="2.6"/><circle cx="12" cy="12" r="3.5" fill="none" stroke="#2a2d36" stroke-width="2.6"/></svg>lorem@silberkranich.investments</li>
        <li><svg viewBox="0 0 24 24"><rect x="2" y="2" width="20" height="20" rx="2" fill="#2a2d36"/></svg>@MusterProfil</li>
      </ul>
    </section>
  </div>
  <footer class="footer-card">
    <div class="footer-brand"><i class="dot"></i><span>Silber Kranich Investments</span></div>
    <p class="footer-claim">Ihr Partner für digitale Werte</p>
    <p class="footer-copy">© 2023 Silber Kranich Investments. Alle Rechte vorbehalten</p>
  </footer>
</article>

</body>
</html>
```